The Web Promotion Playbook for Yard & Patio Construction Crews

We need a book cover design that is for a book targeting landscape and outdoor living contractors that helps them grow their business using online marketing.

We run a business focused on this industry so you can see what we do: https://yardcrewgrowthworks.com/

The title is: The Web Promotion Playbook for Yard & Patio Construction Crews

The author is: Trent Varnholm
Some drafts have been done however they're still looking basic and somewhat amateur, we're looking for something that will stand out.

Target Market(s)

Landscape, Hardscape and Outdoor Living Contractors and Business Owners

Industry/Entity Type

Online Marketing

Font styles to use
Serif
Sans Serif

Requirements
Must have
• The part of the title that should stand out the most is the text "Web Promotion Playbook".
Should not have
• The color red

```html
<!DOCTYPE html>
<html lang="en">
<head>
<meta charset="utf-8">
<title>The Web Promotion Playbook for Yard &amp; Patio Construction Crews</title>
<link rel="stylesheet" href="https://fonts.googleapis.com/css2?family=Bebas+Neue&display=swap">
<style>
  :root {
    --backdrop: #e4e6ec;
    --forest: #015b2c;
    --paper: #f1f2f6;
    --ink: #050505;
    --white: #ffffff;
  }
  html, body {
    margin: 0;
    padding: 0;
    width: 1071px;
    height: 1200px;
    overflow: hidden;
    background: var(--backdrop);
  }
  .book-cover {
    position: absolute;
    left: 125px;
    top: 25px;
    width: 820px;
    height: 1150px;
    display: flex;
    flex-direction: column;
    font-family: "Bebas Neue", "Oswald", sans-serif;
    text-transform: uppercase;
  }
  .title-band {
    height: 150px;
    background: var(--forest);
    color: var(--white);
    display: flex;
    justify-content: center;
    align-items: center;
  }
  .title-band .kicker {
    font-size: 120px;
    line-height: 1;
    letter-spacing: 4px;
    margin: 0;
    padding-top: 10px;
  }
  .title-body {
    flex: 1;
    background: var(--paper);
    display: flex;
    flex-direction: column;
    justify-content: center;
    align-items: center;
  }
  .title-body .line {
    margin: 0;
    line-height: 0.9;
    white-space: nowrap;
  }
  .line-web {
    font-size: 230px;
    color: var(--ink);
  }
  .line-promotion {
    font-size: 200px;
    color: var(--ink);
  }
  .line-playbook {
    font-size: 215px;
    color: var(--forest);
    margin-bottom: 24px !important;
  }
  .line-audience {
    font-size: 88px;
    color: var(--forest);
    letter-spacing: 2px;
    line-height: 0.98 !important;
  }
  .line-audience .amp {
    color: var(--ink);
  }
  .author-band {
    height: 130px;
    background: var(--ink);
    color: var(--white);
    display: flex;
    justify-content: center;
    align-items: center;
    font-size: 64px;
    letter-spacing: 6px;
  }
</style>
</head>
<body>
  <main class="book-cover">
    <header class="title-band">
      <p class="kicker">The</p>
    </header>
    <section class="title-body">
      <p class="line line-web">Web</p>
      <p class="line line-promotion">Promotion</p>
      <p class="line line-playbook">Playbook</p>
      <p class="line line-audience">For Yard <span class="amp">&amp;</span> Patio</p>
      <p class="line line-audience">Construction Crews</p>
    </section>
    <footer class="author-band">Trent Varnholm</footer>
  </main>
</body>
</html>
```